Certificates with Watermark Images

We are looking for a design of One page Certificates with Watermark (background) images where text will be printed over it .
Graphics design is required to reflect the flowing categories:
IPTV (Internet Protocol TV)
VoD (Video on Demand)
Satellite Receiver
Graphics design images for all three categories must be provided to maintain the same them .
Thank you and good luck.
Internet
- Graphics design images for all three categories must be provided to maintain the same them

```html
<!DOCTYPE html>
<html lang="en">
<head>
<meta charset="utf-8">
<title>Certificate of Achievement</title>
<link rel="stylesheet" href="https://fonts.googleapis.com/css2?family=UnifrakturMaguntia&family=EB+Garamond:wght@400;600&display=swap">
<style>
  :root {
    --paper: #f6f3e6;
    --paper-light: #fdfcf7;
    --frame: #a9a9a6;
    --dots: #9d9d9a;
    --ink: #8c8c8a;
    --ink-dark: #7a7a78;
    --title: #8e8e8c;
    --title-shadow: #d2d1cb;
    --rule: #b8b8b4;
    --art-light: #ecebe7;
    --art-mid: #dcdcd8;
    --art-edge: #d0d0cc;
  }
  html, body {
    margin: 0;
    padding: 0;
    width: 849px;
    height: 1200px;
    overflow: hidden;
    background: var(--paper);
  }
  .certificate {
    position: relative;
    width: 849px;
    height: 1200px;
    background: radial-gradient(ellipse 60% 50% at 50% 38%, var(--paper-light) 0%, #faf8ee 45%, var(--paper) 100%);
    font-family: "EB Garamond", "Times New Roman", serif;
    overflow: hidden;
  }
  .frame {
    position: absolute;
    inset: 0;
  }
  .title {
    position: absolute;
    left: 0;
    top: 92px;
    width: 849px;
    height: 140px;
  }
  .title text {
    font-family: "UnifrakturMaguntia", "Times New Roman", serif;
    font-size: 69px;
    fill: var(--title);
  }
  .title .title-shadow { fill: var(--title-shadow); }
  .lead {
    position: absolute;
    left: 0;
    width: 849px;
    margin: 0;
    text-align: center;
    color: var(--ink);
    text-transform: uppercase;
    line-height: 1;
  }
  .lead-main { top: 274px; font-size: 22px; letter-spacing: 4.6px; }
  .lead-sub { top: 301px; font-size: 15.5px; letter-spacing: 4.8px; }
  .rule {
    position: absolute;
    height: 1px;
    background: var(--rule);
  }
  .rule-name { left: 239px; top: 402px; width: 371px; }
  .rule-signature { left: 531px; top: 1097px; width: 238px; }
  .awarded {
    position: absolute;
    left: 0;
    top: 430px;
    width: 849px;
    margin: 0;
    text-align: center;
    font-size: 22px;
    line-height: 1;
    letter-spacing: 4.6px;
    color: var(--ink);
  }
  .awarded .date { font-weight: 600; color: var(--ink-dark); }
  .art {
    position: absolute;
    border-radius: 22px;
    background: linear-gradient(150deg, var(--art-light) 0%, var(--art-mid) 70%, var(--art-edge) 100%);
    box-shadow: 0 0 0 1px rgba(200, 200, 196, 0.35);
    opacity: 0.6;
  }
  .art-satellite { left: 641px; top: 501px; width: 147px; height: 97px; }
  .art-film { left: 125px; top: 617px; width: 298px; height: 181px; }
  .art-tv { left: 622px; top: 769px; width: 133px; height: 157px; }
  .art-dish { left: 107px; top: 983px; width: 100px; height: 128px; }
</style>
</head>
<body>
<main class="certificate">
  <svg class="frame" width="849" height="1200" viewBox="0 0 849 1200" aria-hidden="true">
    <rect x="24.5" y="24.5" width="800" height="1151" fill="none" stroke="var(--frame)" stroke-width="2"/>
    <rect x="33" y="33" width="783" height="1134" fill="none" stroke="var(--dots)" stroke-width="3" stroke-dasharray="0.1 6" stroke-linecap="round"/>
    <rect x="44.5" y="44.5" width="760" height="1111" fill="none" stroke="var(--frame)" stroke-width="1.5"/>
  </svg>

  <svg class="title" viewBox="0 0 849 140" aria-label="Certificate of Achievement">
    <defs>
      <path id="title-arc" d="M60 122 Q424 22 789 122"/>
    </defs>
    <text class="title-shadow" dx="2" dy="3" text-anchor="middle"><textPath href="#title-arc" startOffset="50%">Certificate of Achievement</textPath></text>
    <text text-anchor="middle"><textPath href="#title-arc" startOffset="50%">Certificate of Achievement</textPath></text>
  </svg>

  <p class="lead lead-main">This certificate is proudly</p>
  <p class="lead lead-sub">Presented for honorable achievement to</p>

  <div class="rule rule-name"></div>

  <p class="awarded">AWARDED THIS DAY of <span class="date">11th NOVEMBER, 2011</span></p>

  <div class="art art-satellite" role="img" aria-label="Faint grey satellite illustration"></div>
  <div class="art art-film" role="img" aria-label="Faint grey clapperboard and film reel illustration"></div>
  <div class="art art-tv" role="img" aria-label="Faint grey retro television illustration with an at sign on screen"></div>
  <div class="art art-dish" role="img" aria-label="Faint grey satellite dish illustration"></div>

  <div class="rule rule-signature"></div>
</main>
</body>
</html>
```